Flyer für Therapie- und Gesundheitsdienstleister
Zielgruppe
Therapie- und Gesundheitsdienstleister im Bereich Physiotherapie, Podologie, Prävention und betriebliche Gesundheitsförderung. Für dieses Projekt möchten wir einen Flyer erstellen lassen für die Bewerbung der betrieblichen Gesundheitsförderungen in bzw. für Firmen
Aufgabenstellung
Klare Strukturen, nicht verspielt, DINA4 oder DINA5; leicht medizinischer Touch, evntuell Stockfotos integrieren, edel und hochwertiges Design

```html
<!DOCTYPE html>
<html lang="de">
<head>
<meta charset="utf-8">
<title>Betriebliche Gesundheitsförderung – Flyer</title>
<link href="https://fonts.googleapis.com/css2?family=Montserrat:wght@300;400;500;600;700&display=swap" rel="stylesheet">
<style>
:root{
  --orange:#ec7a0f;
  --ink:#2b2b2b;
  --text:#333;
  --grey-band:#5a5a5c;
  --page-bg:#f1f1f1;
  --white:#fff;
}
*{box-sizing:border-box;margin:0;padding:0}
html,body{width:1200px;height:806px;overflow:hidden;background:var(--white);font-family:'Montserrat',sans-serif;color:var(--text)}
.page{position:absolute;top:39px;width:513px;height:726px;background:linear-gradient(180deg,#f7f7f7 0%,var(--page-bg) 60%,#ececec 100%);box-shadow:0 3px 14px rgba(0,0,0,.28);overflow:hidden}
.page--front{left:47px}
.page--back{left:639px}
.footer-band{position:absolute;left:0;right:0;bottom:0;height:23px;background:var(--grey-band);color:#fff;font-size:8.5px;text-align:center;line-height:23px;letter-spacing:.2px}
.badge{position:absolute;border-radius:50%;background:var(--orange);color:#fff;font-weight:700;text-align:center;display:flex;align-items:center;justify-content:center;box-shadow:0 2px 6px rgba(0,0,0,.25);line-height:1.3}
.front-photo{position:absolute;left:0;top:0}
.badge--front{left:376px;top:239px;width:99px;height:99px;font-size:10px;transform:rotate(-4deg)}
.front-title{position:absolute;left:0;right:0;top:368px;text-align:center;color:var(--orange);font-weight:700;font-size:20.5px;letter-spacing:.2px}
.front-intro{position:absolute;left:28px;right:28px;top:399px;text-align:center;font-size:12.3px;font-weight:300;line-height:17.4px;color:#444}
.front-intro b{font-weight:600;color:var(--ink)}
.need-box{position:absolute;left:29px;top:473px;width:185px;height:202px;background:rgba(255,255,255,.92);border-radius:8px;padding:17px 11px 0 11px;font-size:8.6px;line-height:12.5px;color:#333}
.need-list{list-style:none;margin:13px 0 15px}
.need-list li{display:flex;gap:8px;font-weight:600;margin-bottom:10px}
.need-list .num{color:var(--orange);font-weight:700;font-size:11px}
.front-body{position:absolute;left:239px;top:477px;width:250px;font-size:8.6px;line-height:12.9px;color:#333}
.front-body p+p{margin-top:11px}
.front-body strong{font-weight:700;color:#111}
.back-photo{position:absolute;left:0;top:0}
.badge--back{left:27px;top:9px;width:85px;height:85px;font-size:9px;transform:rotate(-6deg)}
.services-title{position:absolute;left:29px;top:175px;font-size:14px;font-weight:600;color:var(--ink)}
.col{position:absolute;top:200px;font-size:8.4px;line-height:12.9px;color:#333}
.col--left{left:30px;width:225px}
.col--right{left:272px;width:225px}
.sec-title{color:var(--orange);font-weight:600;font-size:10.2px;margin-bottom:8px}
.ticks{list-style:none}
.ticks li{position:relative;padding-left:12px;margin-bottom:4px}
.ticks li::before{content:"";position:absolute;left:1px;top:3px;width:3px;height:6px;border:solid #333;border-width:0 1.3px 1.3px 0;transform:rotate(40deg)}
.col--right .ticks li{margin-bottom:4.3px}
.gap{margin-top:13px}
.col p{margin-bottom:6px}
.cost{position:absolute;left:0;right:0;top:546px;height:157px;background:var(--white)}
.cost-title{position:absolute;left:31px;top:15px;font-size:13.5px;font-weight:600;color:var(--ink)}
.cost-text{position:absolute;left:31px;top:37px;width:270px;font-size:8.3px;line-height:12.9px;color:#333}
.brand{position:absolute;left:312px;top:18px;display:flex;align-items:center;gap:10px}
.brand-mark{width:36px;height:36px;border-radius:50%;background:var(--orange)}
.brand-name{font-size:14.5px;font-weight:500;color:#444;line-height:17px;width:90px}
.contact-photo{position:absolute;left:313px;top:73px;width:52px;height:62px;border-radius:5px}
.contact{position:absolute;left:373px;top:75px;font-size:8.3px;line-height:10.4px;color:#444}
.contact strong{display:block;font-weight:700;color:#222}
.contact .spacer{height:5px}
</style>
</head>
<body>

<section class="page page--front">
  <svg class="front-photo" width="513" height="360" viewBox="0 0 513 360" role="img" aria-label="Foto: lächelnde Mitarbeiterin am Schreibtisch mit Notizbuch, Kollegen im hellen Büro im Hintergrund">
    <defs>
      <linearGradient id="officeTone" x1="0" y1="0" x2="1" y2="1">
        <stop offset="0" stop-color="#dfe3e4"/>
        <stop offset=".45" stop-color="#b9c4c6"/>
        <stop offset="1" stop-color="#e9e7e3"/>
      </linearGradient>
    </defs>
    <path d="M0 0H513V300Q300 385 0 322Z" fill="url(#officeTone)"/>
  </svg>
  <div class="badge badge--front">Jetzt einen<br>persönlichen<br>Termin<br>vereinbaren!</div>

  <h1 class="front-title">Betriebliche Gesundheitsförderung</h1>
  <p class="front-intro">Die betriebliche Gesundheitsförderung hat das Ziel die <b>Gesundheit der Mitarbeiter</b> zu erhalten und zu fördern sowie die <b>Leistungsfähigkeit und Motivation</b> der Belegschaft zu steigern.</p>

  <div class="need-box">
    <p>Immer mehr gewinnen jedoch folgende Punkte an Bedeutung für Unternehmen:</p>
    <ol class="need-list">
      <li><span class="num">1.</span><span>Mitarbeiterbindung &amp;</span></li>
      <li><span class="num">2.</span><span>Arbeitgeber Attraktivität zu erhöhen, um ein Vorteil am Bewerbermarkt zu erzielen.</span></li>
    </ol>
    <p>Auch da können wir Sie mit unserem Know-How und abgerundeten Konzept unterstützen.</p>
  </div>

  <div class="front-body">
    <p>In regelmäßigen Abständen setzen wir uns mit Ihren Mitarbeitern in Verbindung und erfragen den jeweiligen IST Stand und besprechen gemeinsames Vorgehen, um gesundheitliche Problematiken im Handlungsfeld Bewegung und Entspannung präventiv vorzubeugen. Ihre Mitarbeiter werden dadurch in festen monatlichen Intervallen sensibilisiert dass Sie sich um das Wohlbefinden Ihrer Mitarbeiter kümmern und Sie auch darin investieren.</p>
    <p><strong>Sie als Arbeitgeber können nicht wissen und auch zeitlich nicht gewährleisten welche individuellen gesundheitlichen Problematiken Ihre Mitarbeiter haben. Deshalb bieten wir Ihnen eine individuelle Lösung an Dienstleistung, welche den individuellen Bedarf Ihrer Mitarbeiter deckt.</strong></p>
  </div>

  <div class="footer-band">www.physio-kern.de</div>
</section>

<section class="page page--back">
  <svg class="back-photo" width="513" height="159" viewBox="0 0 513 159" role="img" aria-label="Foto: Therapeutin mit Brille im Trainingsraum mit Fitnessgeräten">
    <defs>
      <linearGradient id="gymTone" x1="0" y1="0" x2="1" y2="0">
        <stop offset="0" stop-color="#d9cfc9"/>
        <stop offset=".4" stop-color="#7d7a7c"/>
        <stop offset=".7" stop-color="#e2c9bd"/>
        <stop offset="1" stop-color="#e8d6cf"/>
      </linearGradient>
    </defs>
    <rect width="513" height="159" fill="url(#gymTone)"/>
  </svg>
  <div class="badge badge--back">Jetzt einen<br>persönlichen<br>Termin<br>vereinbaren!</div>

  <h2 class="services-title">Unsere Leistungen</h2>

  <div class="col col--left">
    <h3 class="sec-title">Messung &amp; Analysen</h3>
    <ul class="ticks">
      <li>Messung &amp; Analysen zur individuellen Stress-<br>und Resilienzdiagnostik um zielorientiert ein Stressmanagment in Ihrem Betrieb zu implementieren.</li>
      <li>Dokumentation von Körperdaten und Risiko-<br>faktoren in einer Eingangskontrolle und einem ½ jährlichen Wiederholung der Kontrolle.</li>
      <li>Wirbelsäulen- und Haltungsscreenings, Haltung, Beweglichkeit und Haltungskomponenten werden anschaulich dargestellt und bilden die Basis für zielführende Visualisierung und fundierte Übungsempfehlung.</li>
      <li>Analysen von Körperstabilität und Gleichgewicht; BalanceScan Pro ist ein erprobtes Analysetool für das Thema Körperstabilität</li>
    </ul>
    <h3 class="sec-title gap">Mentale Gesundheit</h3>
    <p>Programme zur Achtsamkeit, Entspannung, und Wahrnehmung. In Kleingruppen, Online</p>
    <h3 class="sec-title gap">Gesundheitstage für Firmen</h3>
    <p>Individuell auf Ihre Firma abgestimmt.</p>
  </div>

  <div class="col col--right">
    <h3 class="sec-title">Bewegungsprogramme:</h3>
    <p>Präventionsprogramme nach §20 zertifiziert<br>von den Krankenkassen wie zum Beispiel:</p>
    <ul class="ticks">
      <li>Entspannungskurse Hatha Yoga</li>
      <li>Pilates</li>
      <li>Rückengymnastik</li>
      <li>Ganzkörper Training an Geräten</li>
      <li>Fit am Arbeitsplatz</li>
      <li>Online-Präventionskurs<br>(zeitlich und räumlich unabhängig)</li>
      <li>und einige mehr....</li>
    </ul>
    <h3 class="sec-title gap">Digitaler Gesundheitscoach</h3>
    <ul class="ticks">
      <li>Workouts</li>
      <li>Live Online- Kurse</li>
      <li>Physio Übungen gezielt und individuell in der Einzelberatung online und persönlich abgestimmt</li>
      <li>Online Präventionscoach<br>oder als Einzelleistung buchbar</li>
      <li>Online Präventionscoach</li>
    </ul>
  </div>

  <div class="cost">
    <h2 class="cost-title">Informationen zu den Kosten</h2>
    <p class="cost-text">Bis zu 600 € können Sie, als Arbeitgeber steuerfrei bezuschussen. Voraussetzung dafür ist, dass die fachlichen Anforderungen der gesetzlichen Krankenkassen erfüllt werden. Diese Leistungen können wir erfüllen und einige mehr on Top. Lassen Sie sich persönlich und individuell beraten und nehmen Sie persönlich oder via E-Mail Kontakt mit uns auf. Senden Sie uns eine E-Mail an wendtmoor@physio-kern.de und wir melden uns umgehend für eine kostenlose Beratung.</p>
    <div class="brand">
      <span class="brand-mark"></span>
      <span class="brand-name">Gesundheitshaus Kern</span>
    </div>
    <svg class="contact-photo" viewBox="0 0 52 62" role="img" aria-label="Porträtfoto der Ansprechpartnerin">
      <defs>
        <linearGradient id="portraitTone" x1="0" y1="0" x2="0" y2="1">
          <stop offset="0" stop-color="#c9c4c0"/>
          <stop offset="1" stop-color="#b7cfae"/>
        </linearGradient>
      </defs>
      <rect width="52" height="62" rx="5" fill="url(#portraitTone)"/>
    </svg>
    <div class="contact">
      <strong>Carla Wendtmoor</strong>
      <strong>Physio Kern Lünen</strong>
      Lindenweg 47<br>44532 Lünen
      <div class="spacer"></div>
      02306 - 12 34 56<br>wendtmoor@physio-kern.de
    </div>
  </div>

  <div class="footer-band">www.physio-kern.de</div>
</section>

</body>
</html>
```